we need a business card design that shows the customer what we can do for them, in pictures and words. we do tipper work of supplying recycled aggregates, soil removal from site, landscaping, demolition & groundwork and much more.(you can find photo`s and a description on our web site - brackleyplant.co.uk)

brackley plant works ltd, family business doing all aspect`s of machine & tipper lorry work.

```html
<!DOCTYPE html>
<html lang="en">
<head>
<meta charset="utf-8">
<title>Brackley Plant Works – Business Card</title>
<link rel="stylesheet" href="https://fonts.googleapis.com/css2?family=Rokkitt:wght@700&display=swap">
<style>
  :root {
    --page: #ffffff;
    --card: #dcdcdc;
    --card-speck: #cfcfcf;
    --ink-blue: #3d5ee0;
    --ink-shadow: rgba(40, 40, 60, 0.35);
    --brand-panel: #ffffff;
    --truck-dark: #2a2b30;
    --truck-mid: #5d616b;
    --truck-light: #b9bcc4;
  }
  * { margin: 0; padding: 0; box-sizing: border-box; }
  html, body {
    width: 1200px; height: 791px; overflow: hidden;
    background: var(--page);
  }
  .canvas { position: relative; width: 1200px; height: 791px; }
  .card {
    position: absolute; left: 35px; top: 92px; width: 1131px; height: 614px;
    background:
      radial-gradient(circle at 30% 40%, var(--card-speck) 0 1px, transparent 1.5px) 0 0 / 5px 5px,
      radial-gradient(circle at 70% 80%, #e6e6e6 0 1px, transparent 1.5px) 0 0 / 7px 7px,
      var(--card);
    overflow: hidden;
  }
  .text {
    position: absolute;
    z-index: 2;
    font-family: "Rokkitt", "Georgia", serif;
    font-weight: 700;
    color: var(--ink-blue);
    text-shadow: 1px 1px 1px var(--ink-shadow);
    white-space: nowrap;
  }
  .brand-panel {
    position: absolute; left: 15px; top: 15px; width: 507px; height: 118px;
    background: var(--brand-panel);
    display: flex; align-items: center; gap: 18px; padding-left: 22px;
  }
  .brand-square { width: 40px; height: 40px; background: var(--ink-blue); flex: none; }
  .brand-name {
    font-family: "Rokkitt", "Georgia", serif; font-weight: 700;
    color: var(--ink-blue); font-size: 42px; line-height: 1.05;
    text-transform: uppercase;
  }
  .tagline { left: 577px; top: 10px; font-size: 29px; line-height: 33px; }
  .service { left: 18px; font-size: 28px; }
  .truck-art {
    position: absolute; z-index: 1;
    left: 585px; top: 150px; width: 530px; height: 245px;
    border-radius: 14px;
    background: linear-gradient(160deg, var(--truck-light) 0%, var(--truck-mid) 45%, var(--truck-dark) 100%);
  }
  .contact { left: 18px; font-size: 27px; }
  .address { left: 18px; font-size: 27px; }
</style>
</head>
<body>
<div class="canvas">
  <section class="card">
    <div class="brand-panel">
      <span class="brand-square"></span>
      <span class="brand-name">Brackley<br>Plant Works</span>
    </div>

    <p class="text tagline">Family buisness doing all aspects of<br>machine and tipper work.<br>email: office@brackleyplant.co.uk</p>

    <div class="truck-art" role="img" aria-label="Illustration of a black tipper lorry carrying the company name"></div>

    <p class="text service" style="top:150px">Soil removal from site</p>
    <p class="text service" style="top:210px">Landscaping</p>
    <p class="text service" style="top:274px">Supplying recycled aggregates</p>
    <p class="text service" style="top:342px">Demolition and ground work and much more</p>

    <p class="text contact" style="top:409px">Robert Hallam - 07700900481 for demolition and groundworks</p>
    <p class="text contact" style="top:481px">Daniel Hallam - 07700900762 for haulage, recycled materials and land restoration</p>
    <p class="text address" style="top:552px">Brackley plant works ltd, 12 Ferndale Row, Ashcombe, Surrey GU9 4QT.  Tel/Fax 01632960418</p>
  </section>
</div>
</body>
</html>
```